Business Card Design for Venture Kite

Venture Kite is a pro bono student consultancy service offered by Corvala KTRB to social start ups and enterprises. We provide consulting services with expertise in areas such as Marketing, IT, Business Strategy and Innovation.
I have attached\ the Venture Kite Logo here for your perusal.
Industry/Entity Type
Business
Contact Information for Business Card
Name: Ha Min Park Name: Thomas Leung
Role: Project Leader Role: Vice Project Leader
M:0477203941 M: 0479352806
E: ha-min.park@corvalaktrb.org E: thomas.leung@corvalaktrb.org
W: www.corvalaktrb.org W: www.corvalaktrb.org

```html
<!DOCTYPE html>
<html lang="en">
<head>
<meta charset="utf-8">
<title>Venture Kite – Business Cards</title>
<link rel="stylesheet" href="https://fonts.googleapis.com/css2?family=Open+Sans:wght@600;800&display=swap">
<style>
  :root {
    --orange: #f47b0c;
    --paper: #f3f2ef;
    --ink: #141414;
    --white: #ffffff;
    --stage: #e6e3de;
  }
  * { box-sizing: border-box; margin: 0; padding: 0; }
  html, body { width: 1200px; height: 601px; overflow: hidden; }
  body {
    background: var(--stage);
    font-family: "Open Sans", Arial, sans-serif;
    display: flex;
    align-items: center;
    justify-content: center;
    gap: 100px;
  }
  .card {
    width: 490px;
    height: 296px;
    display: flex;
    flex-direction: column;
    background: var(--orange);
    box-shadow: 0 6px 16px rgba(0,0,0,0.25);
  }
  .card__name {
    height: 38px;
    display: flex;
    align-items: center;
    justify-content: center;
    color: var(--white);
    font-weight: 600;
    font-size: 19px;
  }
  .card__brand {
    height: 150px;
    background: var(--paper);
    display: flex;
    align-items: center;
    justify-content: center;
    border-bottom: 3px solid rgba(0,0,0,0.12);
  }
  .brand-name {
    color: var(--ink);
    font-weight: 800;
    font-size: 58px;
    letter-spacing: 1px;
    text-transform: uppercase;
  }
  .card__contacts {
    flex: 1;
    list-style: none;
    padding: 12px 0 0 42px;
    display: flex;
    flex-direction: column;
    gap: 8px;
  }
  .contact {
    display: flex;
    align-items: center;
    gap: 14px;
    color: var(--white);
    font-weight: 600;
    font-size: 17px;
  }
  .contact__icon { width: 26px; height: 26px; flex: none; }
  .icon-defs { position: absolute; width: 0; height: 0; }
</style>
</head>
<body>
<svg class="icon-defs" aria-hidden="true">
  <defs>
    <symbol id="icon-phone" viewBox="0 0 26 26">
      <circle cx="13" cy="13" r="12" fill="#fff"/>
      <rect x="9" y="5" width="8" height="16" rx="1.5" fill="#f47b0c"/>
      <rect x="10.5" y="7" width="5" height="10" fill="#fff"/>
      <circle cx="13" cy="19" r="0.9" fill="#fff"/>
    </symbol>
    <symbol id="icon-mail" viewBox="0 0 26 26">
      <circle cx="13" cy="13" r="12" fill="#fff"/>
      <rect x="6" y="8" width="14" height="10" fill="#f47b0c"/>
      <path d="M6.5 8.5 L13 14 L19.5 8.5" fill="none" stroke="#fff" stroke-width="1.4"/>
    </symbol>
    <symbol id="icon-web" viewBox="0 0 26 26">
      <circle cx="13" cy="13" r="12" fill="#fff"/>
      <g fill="none" stroke="#f47b0c" stroke-width="1.5">
        <circle cx="13" cy="13" r="7.5"/>
        <ellipse cx="13" cy="13" rx="3.5" ry="7.5"/>
        <path d="M5.5 13 H20.5 M7 9 H19 M7 17 H19"/>
      </g>
    </symbol>
  </defs>
</svg>

<article class="card">
  <header class="card__name">Ha Min Park ( Project Leader)</header>
  <div class="card__brand"><span class="brand-name">Venture Kite</span></div>
  <ul class="card__contacts">
    <li class="contact"><svg class="contact__icon"><use href="#icon-phone"/></svg>0477203941</li>
    <li class="contact"><svg class="contact__icon"><use href="#icon-mail"/></svg>ha-min.park@corvalaktrb.org</li>
    <li class="contact"><svg class="contact__icon"><use href="#icon-web"/></svg>www.corvalaktrb.org</li>
  </ul>
</article>

<article class="card">
  <header class="card__name">Thomas Leung(Vice Project Leader)</header>
  <div class="card__brand"><span class="brand-name">Venture Kite</span></div>
  <ul class="card__contacts">
    <li class="contact"><svg class="contact__icon"><use href="#icon-phone"/></svg>0479352806</li>
    <li class="contact"><svg class="contact__icon"><use href="#icon-mail"/></svg>thomas.leung@corvalaktrb.org</li>
    <li class="contact"><svg class="contact__icon"><use href="#icon-web"/></svg>www.corvalaktrb.org</li>
  </ul>
</article>
</body>
</html>
```